Modern and professional facebook ad for disability service

Design a facebook ad for a disability service. Want something bright and fun and eyecatching. Would ideally like a carousel ad as this will give us more options to provide information.
CONTENT:
- Looking for a Plan Manager who will support your QRTA journey so that you can focus on living your best possible life and achieve your QRTA Goals?
- Then join the Bluegate Plan Management family today - quick and easy sign up.
- Friendly, Reliable, Responsive Service
- Dedicate Plan Managers so you always speak to the same person
- Fast Payment of Provider Invoices
- Supporting you to live Your Life, Your Way
- Call us today on 1300 482 613
- www.bluegateplanmanagement.com.au

Target Market(s)

Disability Sector

Other font styles liked:
• Raleway

Requirements
Must have
• Bright colours and eye catching design

```html
<!DOCTYPE html>
<html lang="en">
<head>
<meta charset="utf-8">
<title>Bluegate Plan Management – Carousel Ad Concepts</title>
<link rel="stylesheet" href="https://fonts.googleapis.com/css2?family=Gelasio:ital,wght@1,400&family=Poppins:wght@400;500&family=Raleway:wght@700&display=swap">
<style>
  :root {
    --canvas: #ffffff;
    --paper: #efefef;
    --paper-light: #f5f5f5;
    --ink: #1f1f1f;
    --rule: #4a4a4a;
    --brand-pink: #b7336e;
    --brand-teal: #1a9c94;
    --badge-purple: #6b2c84;
    --arc: rgba(255,255,255,0.9);
  }
  * { box-sizing: border-box; margin: 0; padding: 0; }
  html, body { width: 1200px; height: 1200px; overflow: hidden; background: var(--canvas); }
  .board { position: relative; width: 1200px; height: 1200px; font-family: "Poppins", sans-serif; color: var(--ink); }

  .card {
    position: absolute; overflow: hidden;
    background: linear-gradient(135deg, var(--paper-light), var(--paper) 55%, #ebebeb);
  }
  .card .deco { position: absolute; inset: 0; pointer-events: none; }
  .brand {
    position: absolute; left: 12px; top: 14px;
    display: flex; align-items: center; gap: 4px;
    font: 500 11px "Poppins", sans-serif; color: var(--brand-pink);
  }
  .brand-square { width: 9px; height: 9px; background: var(--brand-teal); }
  .top-rule { position: absolute; top: 32px; left: 68px; right: 0; height: 1px; background: var(--rule); opacity: .7; }
  .foot-rule { position: absolute; left: 16px; width: 74%; height: 1px; background: var(--rule); opacity: .5; }
  .foot-url {
    position: absolute; left: 20px;
    font: 400 5px "Gelasio", serif; letter-spacing: 2.1px; color: var(--ink);
  }
  .badge { position: absolute; border-radius: 50%; background: var(--badge-purple); }

  .eyebrow { position: absolute; font-size: 10px; line-height: 1.2; }
  .headline { position: absolute; font: italic 400 22px/1.05 "Gelasio", serif; }
  .body-copy { position: absolute; font-size: 10.5px; line-height: 1.3; }
  .photo { position: absolute; }

  .concept-note {
    position: absolute; left: 102px; top: 910px; width: 520px;
    font: 700 38px/1.22 "Raleway", sans-serif; color: #111;
  }
</style>
</head>
<body>
<div class="board">

  <!-- Slide 1 -->
  <section class="card" style="left:92px;top:60px;width:314px;height:392px;">
    <svg class="deco" viewBox="0 0 314 392"><circle cx="250" cy="230" r="120" fill="none" stroke="var(--arc)" stroke-width="1"/></svg>
    <div class="brand"><span class="brand-square"></span>Bluegate</div>
    <div class="top-rule"></div>
    <p class="eyebrow" style="left:31px;top:71px;font-size:11px;">Looking for a</p>
    <h2 class="headline" style="left:31px;top:87px;font-size:24px;">Plan Manager</h2>
    <p class="body-copy" style="left:31px;top:117px;width:230px;">who will support your QRTA journey so that you can focus on living your best possible life and achieve your QRTA Goals?</p>
    <div class="photo" role="img" aria-label="Photo of a smiling woman in a wheelchair working on a laptop at home" style="left:0;top:191px;width:260px;height:148px;background:linear-gradient(120deg,#c9b9a8,#a5553f 45%,#6b6a4c 75%,#d8d2c8);"></div>
    <div class="foot-rule" style="top:360px;width:235px;"></div>
    <p class="foot-url" style="top:370px;">www.bluegateplanmanagement.com.au</p>
    <div class="badge" style="left:257px;top:336px;width:52px;height:52px;"></div>
  </section>

  <!-- Slide 2 -->
  <section class="card" style="left:449px;top:126px;width:261px;height:327px;">
    <svg class="deco" viewBox="0 0 261 327"><circle cx="200" cy="170" r="110" fill="none" stroke="var(--arc)" stroke-width="1"/></svg>
    <div class="brand"><span class="brand-square"></span>Bluegate</div>
    <div class="top-rule"></div>
    <div class="photo" role="img" aria-label="Photo of a carer helping a smiling older woman in a wheelchair use a laptop" style="left:0;top:61px;width:122px;height:224px;background:linear-gradient(160deg,#9c9c9c,#8fc6c2 40%,#d8b23c 70%,#c9c9c9);"></div>
    <p class="eyebrow" style="left:131px;top:136px;font-size:9.5px;">The join the</p>
    <h2 class="headline" style="left:131px;top:150px;font-size:19px;line-height:1.05;">Bluegate Plan<br>Management<br>family</h2>
    <p class="eyebrow" style="left:131px;top:214px;font-size:9.5px;">today</p>
    <p class="eyebrow" style="left:131px;top:246px;font-size:9.5px;">Quick and easy sign up</p>
    <div class="foot-rule" style="top:300px;width:200px;"></div>
    <p class="foot-url" style="top:309px;font-size:4.5px;letter-spacing:1.8px;">www.bluegateplanmanagement.com.au</p>
    <div class="badge" style="left:214px;top:280px;width:44px;height:44px;"></div>
  </section>

  <!-- Slide 3 -->
  <section class="card" style="left:753px;top:126px;width:259px;height:324px;">
    <svg class="deco" viewBox="0 0 259 324"><circle cx="210" cy="180" r="115" fill="none" stroke="var(--arc)" stroke-width="1"/></svg>
    <div class="brand"><span class="brand-square"></span>Bluegate</div>
    <div class="top-rule"></div>
    <div class="photo" role="img" aria-label="Photo of friends outdoors, one using a wheelchair" style="left:28px;top:60px;width:82px;height:82px;border-radius:50%;background:linear-gradient(135deg,#c9a56a,#3d4e6b 55%,#b23a3a);"></div>
    <div class="photo" role="img" aria-label="Photo of a man in a wheelchair working at an office desk" style="left:62px;top:127px;width:82px;height:82px;border-radius:50%;background:linear-gradient(135deg,#d6d8da,#5a5e66 50%,#e5e5e5);"></div>
    <div class="photo" role="img" aria-label="Photo of a woman with pink hair using a laptop" style="left:28px;top:194px;width:82px;height:82px;border-radius:50%;background:linear-gradient(135deg,#e3e3e3,#c14a8a 40%,#efd8dc);"></div>
    <h2 class="headline" style="left:123px;top:80px;font-size:20px;">Friendly,</h2>
    <h2 class="headline" style="left:149px;top:157px;font-size:20px;">Reliable,</h2>
    <h2 class="headline" style="left:116px;top:222px;font-size:20px;line-height:1;">Responsive<br>Service</h2>
    <div class="foot-rule" style="top:298px;width:190px;"></div>
    <p class="foot-url" style="top:307px;font-size:4.5px;letter-spacing:1.8px;">www.bluegateplanmanagement.com.au</p>
    <div class="badge" style="left:211px;top:276px;width:44px;height:44px;"></div>
  </section>

  <!-- Slide 4 -->
  <section class="card" style="left:237px;top:495px;width:265px;height:331px;">
    <svg class="deco" viewBox="0 0 265 331"><circle cx="215" cy="150" r="100" fill="none" stroke="var(--arc)" stroke-width="1"/></svg>
    <div class="brand"><span class="brand-square"></span>Bluegate</div>
    <div class="top-rule"></div>
    <p class="eyebrow" style="left:26px;top:60px;">Dedicated</p>
    <h2 class="headline" style="left:26px;top:74px;">Plan Manager</h2>
    <p class="body-copy" style="left:26px;top:99px;font-size:9.5px;">so you always speak to the same person</p>
    <div class="photo" role="img" aria-label="Photo of two friends laughing on a bench, one in a wheelchair" style="left:0;top:121px;width:175px;height:176px;border-bottom-right-radius:100%;background:linear-gradient(140deg,#a88f6c,#9fb0cf 45%,#e8b8c8 70%,#6b5a48);"></div>
    <div class="foot-rule" style="top:304px;width:210px;"></div>
    <p class="foot-url" style="top:314px;font-size:4.5px;letter-spacing:1.8px;">www.bluegateplanmanagement.com.au</p>
    <div class="badge" style="left:216px;top:283px;width:44px;height:44px;"></div>
  </section>

  <!-- Slide 5 -->
  <section class="card" style="left:543px;top:495px;width:265px;height:331px;">
    <svg class="deco" viewBox="0 0 265 331"><circle cx="150" cy="140" r="100" fill="none" stroke="var(--arc)" stroke-width="1"/></svg>
    <div class="brand"><span class="brand-square"></span>Bluegate</div>
    <div class="top-rule"></div>
    <div class="photo" role="img" aria-label="Photo of a smiling young man in a cap using a wheelchair outdoors" style="left:0;top:51px;width:229px;height:171px;clip-path:polygon(57px 0,229px 0,154px 171px,0 171px);background:linear-gradient(120deg,#c7ccd2,#8e96a2 40%,#3d6da8 65%,#6f8a5a);"></div>
    <h2 class="headline" style="left:51px;top:229px;">Fast Payment</h2>
    <p class="body-copy" style="left:51px;top:254px;font-size:10px;">of Provider Invoices</p>
    <div class="foot-rule" style="top:304px;width:210px;"></div>
    <p class="foot-url" style="top:314px;font-size:4.5px;letter-spacing:1.8px;">www.bluegateplanmanagement.com.au</p>
    <div class="badge" style="left:216px;top:283px;width:44px;height:44px;"></div>
  </section>

  <!-- Slide 6 -->
  <section class="card" style="left:836px;top:497px;width:264px;height:329px;">
    <svg class="deco" viewBox="0 0 264 329"><circle cx="160" cy="165" r="100" fill="none" stroke="var(--arc)" stroke-width="1"/></svg>
    <div class="brand"><span class="brand-square"></span>Bluegate</div>
    <div class="top-rule"></div>
    <p class="eyebrow" style="left:67px;top:87px;">Supporting you to live</p>
    <h2 class="headline" style="left:116px;top:101px;font-size:21px;line-height:1.03;">Your Life,<br>Your Way</h2>
    <div class="photo" role="img" aria-label="Photo of a family walking at sunset, the mother using a wheelchair" style="left:1px;top:103px;width:187px;height:185px;clip-path:polygon(0 0,105px 0,105px 47px,187px 47px,187px 185px,80px 185px,80px 139px,0 139px);background:linear-gradient(130deg,#f0c98a,#5b5e5c 35%,#7fa7c7 60%,#4f6a3e);"></div>
    <div class="foot-rule" style="top:302px;width:210px;"></div>
    <p class="foot-url" style="top:312px;font-size:4.5px;letter-spacing:1.8px;">www.bluegateplanmanagement.com.au</p>
    <div class="badge" style="left:216px;top:280px;width:44px;height:44px;"></div>
  </section>

  <!-- Slide 7 -->
  <section class="card" style="left:651px;top:850px;width:268px;height:334px;">
    <svg class="deco" viewBox="0 0 268 334"><circle cx="80" cy="150" r="90" fill="none" stroke="var(--arc)" stroke-width="1"/></svg>
    <div class="brand"><span class="brand-square"></span>Bluegate</div>
    <div class="top-rule"></div>
    <div class="photo" role="img" aria-label="Photo of a person in a wheelchair on the beach with arms raised" style="left:41px;top:69px;width:195px;height:98px;border-radius:50% 50% 0 0 / 100% 100% 0 0;background:linear-gradient(180deg,#e8e2d8,#a7b1b3 45%,#c8ab88 75%,#b89a78);"></div>
    <p class="eyebrow" style="left:0;width:268px;text-align:center;top:181px;">Call us today</p>
    <h2 class="headline" style="left:0;width:268px;text-align:center;top:199px;font-size:20px;">1300 482 613</h2>
    <p class="headline" style="left:0;width:268px;text-align:center;top:227px;font-size:13px;">www.bluegateplanmanagement.com.au</p>
    <div class="foot-rule" style="top:305px;width:210px;"></div>
    <p class="foot-url" style="top:315px;font-size:4.5px;letter-spacing:1.8px;">www.bluegateplanmanagement.com.au</p>
    <div class="badge" style="left:219px;top:284px;width:44px;height:44px;"></div>
  </section>

  <p class="concept-note">Pictures used in the proposal is to represent concept only. Client to provide the final pictures</p>
</div>
</body>
</html>
```